Santa Letter 1

This will be a letter from Santa to a child. Themes on the stationary should be Christmas themed. Religious is ok, but want some that aren't. North pole, Santa, Mrs. Clause, Sleigh, Ornaments, etc. We will pick more than 1 winner because we would like 2-3 designs in the end, all being different. High professional quality is very important.

Target Market(s)

Children and parents of young children

Industry/Entity Type

Religious

Font styles to use
Decorative

Requirements
Must have
• Christmas and holiday themes. The page should have space for text to be printed and easily read. So the design should be near the bottom and on one side more than the other so the text can be printed and easily read.

```html
<!DOCTYPE html>
<html lang="en">
<head>
<meta charset="utf-8">
<title>Christmas Letter</title>
<link href="https://fonts.googleapis.com/css2?family=Great+Vibes&display=swap" rel="stylesheet">
<style>
  :root{
    --backdrop:#dcdac6;
    --page:#f1efe6;
    --panel-edge:#ffffff;
    --panel-top:#e9e9e9;
    --panel-mid:#fbfbfa;
    --gold:#b08a2e;
    --gold-dark:#8a6718;
    --gold-light:#d8b860;
    --band:#e6e2d2;
    --band-shine:#f7f5ee;
    --lace:#ecebe6;
    --sticker-red:#d8322a;
  }
  *{margin:0;padding:0;box-sizing:border-box}
  html,body{width:1200px;height:784px;overflow:hidden;background:var(--backdrop)}
  .letter{
    position:absolute;left:330px;top:22px;width:540px;height:740px;
    background:linear-gradient(180deg,var(--page),#ebe8dc);
    box-shadow:0 6px 18px rgba(80,70,40,.25);
    overflow:hidden;
  }
  .lace-border{
    position:absolute;left:0;top:0;width:100%;height:52px;
    background:linear-gradient(180deg,#f8f8f5,var(--lace));
    border-bottom:1px solid #dcdad2;
  }
  .letter-panel{
    position:absolute;left:34px;top:74px;width:472px;height:540px;
    background:radial-gradient(ellipse at 60% 55%,var(--panel-mid) 0%,#f3f3f2 55%,var(--panel-top) 100%);
    box-shadow:0 2px 5px rgba(0,0,0,.15);
  }
  .panel-edge{position:absolute;left:34px;top:74px;width:472px;height:540px;pointer-events:none}
  .title{
    position:absolute;right:62px;top:100px;
    font-family:"Great Vibes",cursive;font-size:54px;font-weight:400;line-height:1;
    color:var(--gold);
    text-shadow:1px 1px 0 #fff,2px 2px 2px rgba(0,0,0,.15);
  }
  .message{
    position:absolute;left:66px;top:172px;width:404px;
    font-family:"Great Vibes",cursive;font-size:23px;line-height:33px;
    color:var(--gold);
  }
  .greeting-band{
    position:absolute;left:0;bottom:0;width:100%;height:118px;
    background:linear-gradient(180deg,var(--band-shine) 0%,var(--band) 45%,#d9d4c0 100%);
    border-top:2px solid #c7b27a;
  }
  .gold-rule{
    position:absolute;left:0;bottom:22px;width:100%;height:4px;
    background:linear-gradient(90deg,var(--gold-dark),var(--gold-light),var(--gold-dark));
  }
  .greeting{
    position:absolute;right:40px;bottom:40px;
    font-family:"Great Vibes",cursive;font-size:44px;line-height:1;
    color:var(--gold);
    text-shadow:1px 1px 0 #fff;
  }
  .sticker{
    position:absolute;left:16px;bottom:96px;width:150px;height:150px;
    border-radius:42% 48% 40% 46%;
    background:radial-gradient(circle at 50% 55%,var(--sticker-red) 0%,#c02a24 55%,#fff 57%,#fff 100%);
    box-shadow:2px 3px 6px rgba(0,0,0,.2);
  }
</style>
</head>
<body>
  <main class="letter">
    <div class="lace-border" role="img" aria-label="White lace border with snowflake scroll pattern"></div>

    <div class="letter-panel"></div>
    <svg class="panel-edge" viewBox="0 0 472 540" aria-hidden="true">
      <rect x="1" y="1" width="470" height="538" fill="none" stroke="var(--panel-edge)" stroke-width="2" stroke-dasharray="6 8"/>
    </svg>

    <h1 class="title">Santa</h1>

    <p class="message">Peace and good will to you and your loved ones this Christmas season. Peace and good will to you and your loved ones this Christmas season. Peace and good will to you and your loved ones this Christmas season. Peace and good will to you and your loved ones this Christmas season. Peace and good will to you and your loved ones this Christmas season.</p>

    <div class="greeting-band">
      <div class="gold-rule"></div>
      <p class="greeting">Merry Christmas</p>
    </div>

    <div class="sticker" role="img" aria-label="Cartoon sticker illustration in red, white and green"></div>
  </main>
</body>
</html>
```